TRK Website

1. A fully functioning website
2. Should be either Linux, windows or Word Press based
3. Intend to have Velmorix host it
4. Photos should reflect diversity (gender/race)

```html
<!DOCTYPE html>
<html lang="en">
<head>
<meta charset="utf-8">
<title>TRK — Tarrow Meridian Group</title>
<link href="https://fonts.googleapis.com/css2?family=Nunito+Sans:wght@700;800&family=Arimo:wght@400;700&display=swap" rel="stylesheet">
<style>
  :root{
    --gold:#786a18;
    --gold-dark:#6b5e12;
    --slate:#2e3d48;
    --ink:#111111;
    --white:#ffffff;
  }
  *{box-sizing:border-box;margin:0;padding:0}
  html,body{width:831px;height:1200px;overflow:hidden;background:var(--white)}
  body{position:relative;font-family:"Arimo",Arial,sans-serif;color:var(--ink)}
  .top-rule{position:absolute;left:0;top:0;width:831px;height:4px;background:var(--gold)}
  .site-header{position:absolute;left:0;top:4px;width:831px;height:79px;background:var(--white)}
  .brand-mark{position:absolute;left:139px;top:12px;width:28px;height:28px;background:var(--gold)}
  .brand-name{position:absolute;left:19px;top:47px;font-family:"Nunito Sans",sans-serif;font-weight:800;font-size:21px;letter-spacing:-0.1px;color:var(--ink);white-space:nowrap}
  .main-nav{position:absolute;left:313px;top:47px;display:flex;align-items:center;height:24px}
  .nav-link{font-size:14px;color:var(--gold);text-decoration:none;margin-right:22px;letter-spacing:.2px}
  .nav-link.is-active{background:var(--gold);color:var(--white);padding:4px 13px;margin-right:13px}
  .nav-phone{display:flex;align-items:center;gap:6px;font-weight:700;font-size:13px;color:var(--gold);margin-left:3px}
  .hero{position:absolute;left:0;top:83px;width:831px;height:465px;overflow:hidden}
  .hero-photo{position:absolute;inset:0;background:
      radial-gradient(ellipse at 55% 40%, #5b6570 0%, transparent 55%),
      linear-gradient(160deg,#2c363f 0%,#3d4851 45%,#27303a 80%,#4a4038 100%)}
  .hero-copy{position:absolute;left:35px;top:256px;width:320px}
  .hero-title{font-weight:700;font-size:27px;line-height:41.5px;color:var(--white);text-shadow:0 1px 3px rgba(0,0,0,.55)}
  .hero-lede{margin-top:4px;font-size:14.5px;line-height:21px;color:var(--white);width:300px}
  .credentials{position:absolute;left:0;top:548px;width:831px;height:169px;background:var(--slate);color:var(--white);text-align:center;font-size:17px;line-height:25.5px;padding:51px 40px 0}
  .services{position:absolute;left:0;top:754px;width:831px}
  .service{position:absolute;top:0;width:205px;text-align:center}
  .service-tile{height:186px;background:var(--gold);color:var(--white);position:relative}
  .service-icon{position:absolute;left:50%;top:30px;transform:translateX(-50%)}
  .service-title{position:absolute;left:0;right:0;top:117px;font-weight:700;font-size:17.5px;line-height:21px;letter-spacing:.3px}
  .service-text{margin-top:16px;font-size:10.5px;line-height:16.5px;padding:0 14px}
  .service-link{display:block;margin-top:1px;font-weight:700;font-size:12px;color:var(--ink);text-decoration:none;letter-spacing:.3px}
  .site-footer{position:absolute;left:0;top:1077px;width:831px;height:123px;background:var(--gold)}
  .footer-mark{position:absolute;left:40px;top:38px;width:34px;height:34px;background:var(--white)}
  .copyright{position:absolute;left:101px;top:48px;font-size:11.5px;color:var(--ink)}
</style>
</head>
<body>
  <div class="top-rule"></div>

  <header class="site-header">
    <span class="brand-mark"></span>
    <span class="brand-name">Tarrow Meridian Group</span>
    <nav class="main-nav">
      <a class="nav-link is-active" href="#">HOME</a>
      <a class="nav-link" href="#">ABOUT US</a>
      <a class="nav-link" href="#">WHAT WE DO</a>
      <a class="nav-link" href="#">CONTACT US</a>
      <span class="nav-phone">
        <svg width="18" height="18" viewBox="0 0 18 18" aria-hidden="true">
          <circle cx="9" cy="9" r="8" fill="none" stroke="currentColor" stroke-width="1.4"/>
          <path d="M6 5.2l1.5-.4.9 2-1 .8a6 6 0 0 0 2.9 2.9l.8-1 2 .9-.4 1.5c-3.6.3-7-3.1-6.7-6.7z" fill="currentColor"/>
        </svg>
        202-555-0148
      </span>
    </nav>
  </header>

  <section class="hero">
    <div class="hero-photo" role="img" aria-label="Photo of a diverse team in a meeting room, a woman placing sticky notes on a dark wall planning board while colleagues watch"></div>
    <div class="hero-copy">
      <h1 class="hero-title">Helping Public Sector Organizations Work Smarter</h1>
      <p class="hero-lede">TRK is a public sector focused management consulting firm providing facilitation and advisory support services.</p>
    </div>
  </section>

  <section class="credentials">
    TRK is able to bring to any engagement experienced consultants with decades of knowledge and experience garnered from working at all levels of government as chief financial officer, chief procurement officer, chief operating officer and as city manager.
  </section>

  <section class="services">
    <article class="service" style="left:73px">
      <div class="service-tile">
        <svg class="service-icon" width="70" height="68" viewBox="0 0 70 68" aria-hidden="true">
          <path d="M10 3h50a7 7 0 0 1 7 7v32a7 7 0 0 1-7 7H24L8 64V49h0a7 7 0 0 1-5-7V10a7 7 0 0 1 7-7z" fill="none" stroke="#fff" stroke-width="4" stroke-linejoin="round"/>
          <g stroke="#fff" stroke-width="2.4" fill="none" stroke-linecap="round">
            <path d="M17 30l5 5M22 30l-5 5M36 12l4 4M40 12l-4 4"/>
            <circle cx="34" cy="27" r="3.2"/>
            <path d="M24 40c8 0 18-4 22-16"/><path d="M42 24l4-1 1 4"/>
          </g>
        </svg>
        <h2 class="service-title">STRATEGIC<br>PLANNING</h2>
      </div>
      <p class="service-text">Custom fit to the organization and the business situation at hand.</p>
      <a class="service-link" href="#">LEARN MORE</a>
    </article>

    <article class="service" style="left:311px">
      <div class="service-tile">
        <svg class="service-icon" width="60" height="66" viewBox="0 0 60 66" aria-hidden="true">
          <g fill="#fff">
            <rect x="2" y="50" width="5" height="14"/><rect x="10" y="46" width="5" height="18"/>
            <rect x="18" y="42" width="5" height="22"/><rect x="26" y="36" width="5" height="28"/>
            <rect x="34" y="30" width="5" height="34"/><rect x="42" y="22" width="6" height="42"/>
            <path d="M2 46C24 42 40 30 46 14l-6-2L55 2l3 18-6-4C45 34 26 46 2 48z"/>
          </g>
        </svg>
        <h2 class="service-title">PERFORMANCE<br>MANAGEMENT</h2>
      </div>
      <p class="service-text">Improved quality of customer service and reduced turnaround times.</p>
      <a class="service-link" href="#">LEARN MORE</a>
    </article>

    <article class="service" style="left:549px">
      <div class="service-tile">
        <svg class="service-icon" width="58" height="62" viewBox="0 0 58 62" aria-hidden="true">
          <g fill="#fff">
            <rect x="4" y="32" width="9" height="22"/><rect x="17" y="24" width="9" height="30"/>
            <rect x="30" y="30" width="9" height="24"/><rect x="43" y="18" width="9" height="36"/>
            <rect x="0" y="56" width="56" height="4"/>
          </g>
          <path d="M3 24l14-10 13 9 18-17" fill="none" stroke="#fff" stroke-width="3"/>
          <path d="M43 3h10v10z" fill="#fff"/>
        </svg>
        <h2 class="service-title">DATA<br>ANALYTICS</h2>
      </div>
      <p class="service-text">Direct cost reductions and cost avoidance revenue enhancements, and goodwill.</p>
      <a class="service-link" href="#">LEARN MORE</a>
    </article>
  </section>

  <footer class="site-footer">
    <span class="footer-mark"></span>
    <p class="copyright">Copyright 2018. Tarrow Meridian Group</p>
  </footer>
</body>
</html>
```